Design the Marketing Brochure for a service company with Zenith 500 Clients

We need to redesign our marketing brochures to reflect the new service lines we have added in the last few years. We are a professional staffing firm based in Miami, Florida and have a portfolio of clients that include: Velmora Seaways, Tidewell Voyage Lines, Grillano Foods Corp, Horizon Lens Network Etc. I have attached our current marketing inserts in pdf format. I would like to have 5 inserts displaying our services, process and business lines.

Target Market(s)

Zenith 1000 companies. Within those companies our clients are: CFO's, VP of Finance, Controller, Head of Human Resources, Banking Executives etc. All financial related roles.

Industry/Entity Type

Recruitment

Colors
ec1f27
ffffff
aaaaaa
fece3e
000000

Requirements
Must have
• 5 pages 3 of which we have mots of the content. One page dedicated to " Temporary Staffing" and one page dedicated to our "Banking Division" The brochures should include professional pictures and a well designed layout that looks professional and appealing to an educated client. Our colors are Red, Gray and White.
• Please see our attached brochures and our website at www.kvtrecruit.example
Nice to have
• Professional pictures of people in the business workplace.
Should not have
• Graphics or cartoons of any kind.

```html
<!DOCTYPE html>
<html lang="en">
<head>
<meta charset="utf-8">
<title>Kestvale Talent Partners – Human Capital Solutions Brochure</title>
<link rel="stylesheet" href="https://fonts.googleapis.com/css2?family=Montserrat:wght@700;900&family=Open+Sans:wght@400;600&display=swap">
<style>
  :root {
    --red: #9e1d25;
    --yellow: #f3c94a;
    --white: #ffffff;
    --gray: #aaaaaa;
    --ink: #1d1d1d;
    --backdrop: #f3eeee;
  }
  * { box-sizing: border-box; margin: 0; padding: 0; }
  html, body { width: 1200px; height: 824px; overflow: hidden; }
  body { background: var(--backdrop); font-family: "Open Sans", sans-serif; position: relative; }

  .page { position: absolute; top: 22px; width: 552px; height: 780px; overflow: hidden; background: var(--white); box-shadow: 0 6px 18px rgba(0,0,0,.12); }
  .page--back { left: 48px; }
  .page--front { left: 600px; }

  /* Wordmark: invented name, one colour, one weight */
  .wordmark { font-family: "Montserrat", sans-serif; font-weight: 700; font-size: 19px; color: var(--red); letter-spacing: .3px; line-height: 1; white-space: nowrap; }

  /* Back cover */
  .back-photo { position: absolute; inset: 0; background: linear-gradient(160deg, #d9d9db 0%, #f4f4f4 45%, #e2e2e2 70%, #bdbdbf 100%); }
  .info-panel { position: absolute; top: 70px; left: 0; width: 500px; height: 300px; background: var(--red); clip-path: polygon(0 0, 100% 0, 92% 100%, 0 100%); padding: 0 44px 0 22px; }
  .info-panel__heading { background: var(--yellow); color: var(--red); font-family: "Montserrat", sans-serif; font-weight: 700; font-size: 17px; margin: 22px -44px 12px -22px; padding: 8px 22px; clip-path: polygon(0 0, 94% 0, 91% 100%, 0 100%); }
  .info-panel p { color: var(--white); font-size: 10.2px; line-height: 1.35; margin-bottom: 6px; text-align: justify; }

  .back-footer { position: absolute; left: 0; bottom: 0; width: 100%; height: 230px; }
  .back-footer__shapes { position: absolute; inset: 0; width: 100%; height: 100%; }
  .back-footer .wordmark { position: absolute; left: 24px; top: 62px; }
  .contact { position: absolute; left: 24px; top: 108px; list-style: none; }
  .contact li { display: flex; align-items: center; gap: 9px; font-size: 12px; color: var(--ink); line-height: 17px; }
  .contact__icon { width: 12px; height: 12px; flex: none; fill: var(--ink); }
  .back-url { position: absolute; left: 0; right: 0; bottom: 18px; text-align: center; color: var(--white); font-family: "Montserrat", sans-serif; font-weight: 700; font-size: 15px; letter-spacing: 3px; }

  /* Front cover */
  .front-shapes { position: absolute; inset: 0; width: 100%; height: 100%; }
  .front-cover .wordmark { position: absolute; top: 32px; right: 30px; font-size: 21px; }
  .front-title { position: absolute; left: 118px; top: 452px; font-family: "Montserrat", sans-serif; font-weight: 900; color: var(--red); line-height: .92; }
  .front-title__line--lg { display: block; font-size: 66px; letter-spacing: 1px; }
  .front-title__line--sm { display: block; font-size: 30px; padding-left: 82px; }
  .front-title__line--md { display: block; font-size: 46px; }
  .front-lines { position: absolute; left: 0; right: 0; top: 636px; text-align: center; font-family: "Montserrat", sans-serif; font-weight: 700; font-size: 19px; color: var(--red); }
</style>
</head>
<body>

<section class="page page--back" aria-label="Back cover">
  <div class="back-photo" role="img" aria-label="Photo of a hand on a computer mouse at an office desk"></div>

  <div class="info-panel">
    <h2 class="info-panel__heading">When top performers lack the know-how</h2>
    <p>You know who your top performers are. They're your go-to accounting professionals who would be in the CPA Guild All-Star Game every year, if one existed. But sometimes even they can't handle the specialized tasks that arise, such as evaluating the tax implications of a new overseas location or preparing for an upcoming systems conversion. This is the perfect time to call a few trusted temp staffing agencies.</p>
    <p>A specialized temporary accounting professional can come in for the duration of the project and provide the expertise your core team lacks. He or she can even train your team members so they can handle similar situations in the future. Many highly skilled and experienced professionals choose to work on an interim basis because of the variety and flexibility this career path provides.</p>
    <p>Temp staffing agencies offer you a way to handle increased business, heavy workloads or specialty projects that may lie beyond the experience or capacity of your current staff. Calling in the specialists these firms represent could be the short-term support you need to maintain your organization's long-term success.</p>
  </div>

  <div class="back-footer">
    <svg class="back-footer__shapes" viewBox="0 0 552 230" preserveAspectRatio="none">
      <polygon points="0,48 552,14 552,22 0,56" fill="var(--yellow)"/>
      <polygon points="0,56 552,22 552,90 0,98" fill="var(--white)"/>
      <polygon points="0,98 552,90 552,168 0,182" fill="var(--yellow)"/>
      <polygon points="0,182 552,168 552,230 0,230" fill="var(--red)"/>
    </svg>
    <div class="wordmark">Kestvale Talent Partners</div>
    <ul class="contact">
      <li><svg class="contact__icon" viewBox="0 0 12 12"><path d="M6 0a4 4 0 0 0-4 4c0 3 4 8 4 8s4-5 4-8a4 4 0 0 0-4-4zm0 5.5A1.5 1.5 0 1 1 6 2.5a1.5 1.5 0 0 1 0 3z"/></svg>1450 NW 22 Avenue Suite 310 Miami, FL 33125</li>
      <li><svg class="contact__icon" viewBox="0 0 12 12"><path d="M2.5 0.5l2 2.5-1 1.5c.8 1.6 2 2.8 3.5 3.5l1.5-1 2.5 2-1 2C5 11 1 7 .5 2.5z"/></svg>(305) 555-0148</li>
      <li><svg class="contact__icon" viewBox="0 0 12 12"><path d="M0 2h12v8H0zm1 1v.3l5 3.4 5-3.4V3z"/></svg>info@kvtrecruit.example</li>
    </ul>
    <div class="back-url">www.kvtrecruit.example</div>
  </div>
</section>

<section class="page page--front front-cover" aria-label="Front cover">
  <svg class="front-shapes" viewBox="0 0 552 780" preserveAspectRatio="none">
    <defs>
      <radialGradient id="warmGlow" cx="55%" cy="40%" r="70%">
        <stop offset="0" stop-color="#fff3c2"/>
        <stop offset=".45" stop-color="#f1bd5a"/>
        <stop offset="1" stop-color="#a8441c"/>
      </radialGradient>
    </defs>
    <polygon points="40,80 552,80 552,405 80,435" fill="url(#warmGlow)" role="img" aria-label="Photo of two hands joining puzzle pieces against warm light"/>
    <polyline points="80,435 552,405" stroke="var(--yellow)" stroke-width="7" fill="none"/>
    <polygon points="0,50 40,80 80,435 55,600 0,605" fill="var(--red)"/>
    <polygon points="0,600 552,575 552,587 0,612" fill="var(--yellow)"/>
    <polygon points="0,612 552,587 552,607 0,627" fill="var(--red)"/>
    <polygon points="0,627 552,607 552,670 0,690" fill="var(--yellow)"/>
    <polygon points="0,690 552,670 552,780 0,780" fill="var(--red)"/>
  </svg>

  <div class="wordmark">Kestvale Talent Partners</div>

  <h1 class="front-title">
    <span class="front-title__line--lg">HUMAN</span>
    <span class="front-title__line--sm">CAPITAL</span>
    <span class="front-title__line--md">SOLUTIONS</span>
  </h1>

  <p class="front-lines">Accounting, Finance, Banking and HR</p>
</section>

</body>
</html>
```